Rinzo Pizza & Pasta Takeaway Flyer

Our takeaway shop needs a well designed flyer for print and letter box distribution. Design to have a clear list of menu, Specials, contact details. If menu doesn't fit into A4, we won't mind going upto extended A4. I have attached draft copy of our menu and list of item in excel. Please add 5mm Bleed to the flyer.
Flyer will get printed on 115gsm Gloss stock.

```html
<!DOCTYPE html>
<html lang="en">
<head>
<meta charset="utf-8">
<title>Rinzo Pizza &amp; Pasta – Takeaway Menu</title>
<link href="https://fonts.googleapis.com/css2?family=Oswald:wght@500;600&family=Questrial&display=swap" rel="stylesheet">
<style>
:root{
  --wood-dark:#6e2913;
  --wood:#9a4423;
  --wood-light:#b5582c;
  --panel:rgba(70,20,6,.28);
  --green:#6dac3d;
  --text:#fbefe4;
  --desc:#ecc7ad;
  --ink:#111;
  --white:#fff;
}
*{box-sizing:border-box;margin:0;padding:0}
html,body{width:1032px;height:1200px;overflow:hidden;background:var(--white)}
body{font-family:"Questrial",sans-serif;color:var(--text)}
.sheet{position:relative;width:1200px;height:1396px;transform:scale(.86);transform-origin:0 0}
.page-label{position:absolute;left:0;width:1200px;text-align:center;font-family:"Questrial",sans-serif;color:var(--ink);font-size:78px;line-height:1;z-index:3}
.page{position:absolute;left:0;width:1200px;background:
  linear-gradient(180deg,rgba(0,0,0,.08),rgba(255,255,255,.04) 30%,rgba(0,0,0,.1) 60%,rgba(255,255,255,.05)),
  linear-gradient(90deg,var(--wood-dark),var(--wood) 20%,var(--wood-light) 50%,var(--wood) 80%,var(--wood-dark))}
.page-one{top:45px;height:638px}
.page-two{top:763px;height:633px}
.photo{position:absolute}
.photo-pizza-one{left:800px;top:300px;width:400px;height:338px;background:radial-gradient(circle at 70% 60%,rgba(236,170,70,.75),rgba(200,90,40,.45) 45%,rgba(154,68,35,0) 70%)}
.photo-pizza-two{left:0;top:270px;width:330px;height:363px;background:radial-gradient(circle at 40% 45%,rgba(232,150,70,.7),rgba(190,80,40,.4) 45%,rgba(154,68,35,0) 72%)}
.photo-plate{left:900px;top:410px;width:300px;height:223px;background:radial-gradient(circle at 60% 80%,#f4f4f2,#cfcfcc 55%,rgba(160,160,160,0) 75%)}
.col{position:absolute;background:var(--panel);padding:0 6px 6px;display:flex;flex-direction:column}
.head{flex:none;background:var(--green);color:var(--white);font-family:"Oswald",sans-serif;font-weight:600;text-transform:uppercase;font-size:27px;line-height:1;padding:4px 6px;display:flex;align-items:center;justify-content:space-between;margin:0 -6px}
.head .price{font-family:"Questrial",sans-serif;font-weight:400;font-size:24px;text-transform:none}
.head small{font-family:"Questrial",sans-serif;font-size:14px;text-transform:none;display:block;font-weight:400;margin-top:2px}
.sizes{display:grid;grid-template-columns:repeat(3,40px);text-align:center;font-family:"Questrial",sans-serif;font-weight:400}
.sizes b{font-size:10px;font-weight:400}
.sizes span{font-size:15px}
.list{flex:none;display:flex;flex-direction:column;justify-content:space-between}
.list.fill{flex:1;min-height:0}
.item{line-height:1}
.row{display:flex;align-items:baseline}
.nm{font-size:16px;white-space:nowrap}
.dots{flex:1;border-bottom:2px dotted var(--text);margin:0 3px;transform:translateY(-3px)}
.pr{font-size:15px}
.ds{font-size:10px;color:var(--desc);line-height:1.1;margin-top:1px}
.grid2{flex:none;display:grid;grid-template-columns:1fr 1fr;column-gap:10px;row-gap:8px}
.note{font-size:8px;text-align:right;color:var(--desc);line-height:1.3}
.contact{background:var(--green);color:var(--white);margin:0 -6px -6px;padding:6px 8px;font-size:18px;line-height:1.2}
.contact h3{font-family:"Oswald",sans-serif;font-weight:600;font-size:26px;text-transform:uppercase;margin-bottom:4px}
.contact .phone{font-size:22px}
.terms{font-size:10px;color:var(--desc);line-height:1.2}
.brand{position:absolute;left:1040px;top:510px;display:flex;align-items:center;gap:8px;font-family:"Oswald",sans-serif;font-weight:600;font-size:24px;color:#c8262b}
.brand i{display:block;width:30px;height:30px;border-radius:50%;background:#c8262b}
</style>
</head>
<body>
<div class="sheet">
  <div class="page-label" style="top:-4px">1st Page</div>
  <div class="page-label" style="top:686px">2nd page</div>

  <section class="page page-one">
    <div class="photo photo-pizza-one" role="img" aria-label="Photo of a pizza on a wooden board"></div>

    <div class="col" style="left:5px;top:13px;width:255px;height:620px">
      <div class="head">Starter</div>
      <div class="list" style="height:305px;margin-top:6px">
        <div class="item"><div class="row"><span class="nm">Garlic Bread</span><span class="dots"></span><span class="pr">3.95</span></div></div>
        <div class="item"><div class="row"><span class="nm">Cheesy Garlic Bread</span><span class="dots"></span><span class="pr">5.5</span></div></div>
        <div class="item"><div class="row"><span class="nm">Sweet Chilli Cheese Pizza</span><span class="dots"></span><span class="pr">7.95</span></div><div class="ds">Sweet Chilli Sauce Base topped with Cheese &amp; Herbs</div></div>
        <div class="item"><div class="row"><span class="nm">Chips (Lge+S2)</span><span class="dots"></span><span class="pr">4.95</span></div><div class="ds">with Tomato Sauce</div></div>
        <div class="item"><div class="row"><span class="nm">Chips &amp; Gravy</span><span class="dots"></span><span class="pr">6.95</span></div></div>
        <div class="item"><div class="row"><span class="nm">Beer Battered Chips</span><span class="dots"></span><span class="pr">6.95</span></div></div>
        <div class="item"><div class="row"><span class="nm">Curly Fries (Lge+$2.5)</span><span class="dots"></span><span class="pr">5.95</span></div><div class="ds">with Ranch Dip</div></div>
        <div class="item"><div class="row"><span class="nm">Sweet Potato Chips</span><span class="dots"></span><span class="pr">6.95</span></div><div class="ds">with Garlic Aioli Sauce</div></div>
        <div class="item"><div class="row"><span class="nm">Onion Rings</span><span class="dots"></span><span class="pr">6.5</span></div><div class="ds">with Ranch Dip</div></div>
        <div class="item"><div class="row"><span class="nm">Chicken Nuggets (8pcs)</span><span class="dots"></span><span class="pr">4.95</span></div><div class="ds">with Tomato Sauce</div></div>
        <div class="item"><div class="row"><span class="nm">Pepper Squid</span></div><div class="ds">with Lemon Wedge</div></div>
        <div class="item"><div class="row"><span class="nm">Chicken Chilli</span><span class="dots"></span><span class="pr">7.95</span></div><div class="ds">with Lemon Wedge &nbsp;&nbsp;&nbsp;&nbsp;&nbsp;&nbsp;**Add Extra Sauce 50.75</div></div>
      </div>
      <div class="head" style="margin-top:12px">Garlic Sub <span class="price">$9.95</span></div>
      <div class="list fill" style="margin-top:6px">
        <div class="item"><div class="nm">Pulled Beef</div><div class="ds">Cheese, Pulled Beef, Salami, Onion, Mushroom with BBQ Sauce</div></div>
        <div class="item"><div class="nm">Chicken</div><div class="ds">Cheese, Seasoned Chicken, Tomato, Onion, Fetta with Sweet Chilli Sauce</div></div>
        <div class="item"><div class="nm">Veg</div><div class="ds">Cheese, Tomato, Onion, Mushroom, Capsicum, Pineapple with Tomato Sauce</div></div>
        <div class="item"><div class="nm">Meat</div><div class="ds">Cheese, Ham, Pepperoni, Salami, Chorizo with BBQ Sauce</div></div>
        <div class="item"><div class="nm">Bacon &amp; Chicken</div><div class="ds">Cheese, Seasoned Chicken, Bacon, Mushroom with Peri Peri Sauce</div></div>
      </div>
    </div>

    <div class="col" style="left:267px;top:13px;width:315px;height:620px">
      <div class="head"><span>Lite</span><span class="sizes"><b>SMALL</b><b>LARGE</b><b>FAMILY</b><span>9</span><span>13</span><span>20</span></span><span style="width:60px"></span></div>
      <div class="grid2" style="margin-top:8px">
        <div class="item"><div class="nm">Hawaiian</div><div class="ds">Cheese, Ham &amp; Pineapple</div></div>
        <div class="item"><div class="nm">Margherita</div><div class="ds">Cheese, Tomatoes, Basil &amp; Oregano</div></div>
        <div class="item"><div class="nm">Mozzy</div><div class="ds">Cheese</div></div>
        <div class="item"><div class="nm">New Yorker</div><div class="ds">Pepperoni, Basil &amp; Oregano</div></div>
        <div class="item" style="grid-column:1/3"><div class="nm">Veggie</div><div class="ds">Onion, Tomato, Mushroom, Capsicum, Olives, Pineapple, Basil &amp; Oregano</div></div>
      </div>
      <div class="head" style="margin-top:10px"><span style="width:30px"></span><span class="sizes"><b>SMALL</b><b>LARGE</b><b>FAMILY</b><span>13</span><span>19</span><span>25</span></span><span>Classic</span></div>
      <div class="list fill" style="margin-top:8px">
        <div class="item"><div class="nm">Supreme</div><div class="ds">Cheese, Pepperoni, Ham, Beef, Onion, Olives, Capsicum, Pineapple &amp; Mushroom</div></div>
        <div class="item"><div class="nm">Meat Lovers</div><div class="ds">Cheese, Pepperoni, Salami, Ham, Bacon, Chorizo &amp; BBQ Sauce</div></div>
        <div class="item"><div class="nm">Ozzy</div><div class="ds">Cheese, Chorizo, Bacon, Onion &amp; Egg</div></div>
        <div class="item"><div class="nm">BBQ Chicken</div><div class="ds">Cheese, Chicken, Bacon, Mushroom &amp; BBQ Sauce</div></div>
        <div class="item"><div class="nm">Tropical Chicken</div><div class="ds">Cheese, Chicken, Ham, Pineapple</div></div>
        <div class="item"><div class="nm">Outback</div><div class="ds">Cheese, Ham, Salami, Bacon, Mushroom &amp; Onion</div></div>
        <div class="item"><div class="nm">Spicy Pizza</div><div class="ds">Cheese, Pepperoni, Onion, Jalapenos &amp; Chilli Flakes</div></div>
        <div class="item"><div class="nm">Mexican</div><div class="ds">Cheese, Beef, Pepperoni, Onion, Roasted Capsicum, Jalapenos, Chilli &amp; Sourcream</div></div>
        <div class="item"><div class="nm">Capricciosa</div><div class="ds">Cheese, Ham, Salami, Mushroom, Tomato &amp; Olives</div></div>
        <div class="item"><div class="nm">Veg Supreme</div><div class="ds">Cheese, Tomato, Onion, Mushroom, Roasted Capsicum, Pineapple, Fetta, Jalapenos &amp; Chilli</div></div>
        <div class="item"><div class="nm">Four Cheese</div><div class="ds">Cheese, Fetta, Bocconcini, Parmesan &amp; Basil</div></div>
      </div>
    </div>

    <div class="col" style="left:592px;top:13px;width:306px;height:620px">
      <div class="head"><span style="width:30px"></span><span class="sizes"><b>SMALL</b><b>LARGE</b><b>FAMILY</b><span>13</span><span>19</span><span>25</span></span><span>Premium</span></div>
      <div class="list" style="height:370px;margin-top:10px">
        <div class="item"><div class="nm">Garden Gourmet</div><div class="ds">Cheese, Semi-dried tomato, Mushrooms, Onion, Roasted Capsicum, Olives, Cherry Tomato, Spinach, Bocconcini &amp; Basil</div></div>
        <div class="item"><div class="nm">Paneer Tikka</div><div class="ds">Cheese, Marinated Paneer, Onion, Tomato, Capsicum, Olives &amp; Corinander</div></div>
        <div class="item"><div class="nm">Pesto Chicken</div><div class="ds">Cheese, Chicken, Sun-Dried Tomato, Onion, Fetta &amp; Parsley</div></div>
        <div class="item"><div class="nm">Butter Chicken</div><div class="ds">Cheese, Marinated Chicken, Onion, Capsicum, Corinader, Cashew &amp; Lemon Wedge</div></div>
        <div class="item"><div class="nm">Meat &amp; Chicken</div><div class="ds">Pulled Beef, Pepperoni, Chicken, Salami, Roasted Capsicum, Mushroom, Onion &amp; BBQ Sauce</div></div>
        <div class="item"><div class="nm">Mediterranean</div><div class="ds">Pepperoni, Roasted Capsicum, Mushroom, Chorizo, Olives, Fetta &amp; Bocconcini</div></div>
        <div class="item"><div class="nm">The Lot</div><div class="ds">Ham, Pepperoni, Salami, Pulled Beef, Sausage, Capsicum, Onion, Olives, Tomato, Pineapple, Basil &amp; Oregano</div></div>
      </div>
      <div class="head" style="margin-top:12px"><span>Seafood</span><span class="sizes"><b>SMALL</b><b>LARGE</b><b>FAMILY</b><span>14</span><span>21</span><span>28</span></span></div>
      <div class="list fill" style="margin-top:8px">
        <div class="item"><div class="nm">The Pacific</div><div class="ds">Seafood Mix, Mushrooms, Roasted Capsicum &amp; Garlic Oil (Anchovies Suggested)</div></div>
        <div class="item"><div class="nm">Reef n Turf</div><div class="ds">Prawn, Pulled Beef, Onion, Mushroom, Capsicum, Olives &amp; Garlic Sauce</div></div>
        <div class="item"><div class="nm">Prawn &amp; Garlic</div><div class="ds">Prawns, Cherry Tomato, Spinach, Bocconcini &amp; Garlic Sauce</div></div>
      </div>
      <div class="note" style="margin-top:4px">** Thin Base Available<br>** GF base available only in large size. Extra $3<br>** Each Extra Topping - Small $1, Large $2, Family $3</div>
    </div>

    <div class="col" style="left:906px;top:13px;width:290px;height:620px">
      <div class="head">Calzone</div>
      <div class="list" style="height:90px;margin-top:8px">
        <div class="item"><div class="row"><span class="nm">Classic Calzone</span><span class="dots"></span><span class="pr">16</span></div><div class="ds">Folded Pizza, Rolled &amp; Cooked, Sealing in all Flavours from Classic Pizza range.</div></div>
        <div class="item"><div class="row"><span class="nm">Premium Calzone</span><span class="dots"></span><span class="pr">18</span></div><div class="ds">Folded Pizza, Rolled &amp; Cooked, Sealing in all Flavours from Premium Pizza range.</div></div>
      </div>
      <div class="head" style="margin-top:22px">Pasta</div>
      <div class="list fill" style="margin-top:8px">
        <div class="item"><div class="row"><span class="nm">Napoletana</span><span class="dots"></span><span class="pr">14</span></div><div class="ds">Tomatoes, Onions, and Special Italian Herbs in Red Pasta sauce</div></div>
        <div class="item"><div class="row"><span class="nm">Vegetaria</span><span class="dots"></span><span class="pr">16</span></div><div class="ds">Mushroom, Tomatoes, Onions, Capsicum and Special Italian Herbs in Red Pasta sauce</div></div>
        <div class="item"><div class="row"><span class="nm">Bolognese</span><span class="dots"></span><span class="pr">16</span></div><div class="ds">Traditional Beef, Onions and Special Italian Herbs in Red Pasta sauce</div></div>
        <div class="item"><div class="row"><span class="nm">Carbonara</span><span class="dots"></span><span class="pr">16</span></div><div class="ds">Bacon, Eggs &amp; Mushrooms in a Creamy White Sauce</div></div>
        <div class="item"><div class="row"><span class="nm">Alla Panna</span><span class="dots"></span><span class="pr">16</span></div><div class="ds">Ham &amp; Mushrooms in a Creamy White Sauce</div></div>
        <div class="item"><div class="row"><span class="nm">Chicken Carbonara</span><span class="dots"></span><span class="pr">16</span></div><div class="ds">Chicken, Eggs, Mushrooms &amp; Onions in a Creamy White Sauce</div></div>
        <div class="item"><div class="row"><span class="nm">Chicken</span><span class="dots"></span><span class="pr">16</span></div><div class="ds">Chicken, Tomato, Pesto in a Creamy White Sauce</div></div>
        <div class="item"><div class="row"><span class="nm">Greek Chicken</span><span class="dots"></span><span class="pr">16</span></div><div class="ds">Chicken, Tomato, Fetta, Olives in a Red Pasta Sauce</div></div>
        <div class="item"><div class="row"><span class="nm">Garlic Prawn</span><span class="dots"></span><span class="pr">18</span></div><div class="ds">Prawn, Garlic, Onion, Lemon in a Creamy White Sauce</div></div>
        <div class="item"><div class="row"><span class="nm">Puttanesca</span><span class="dots"></span><span class="pr">18</span></div><div class="ds">Anchovies, Olives, Capers in a Red Pasta Sauce</div></div>
        <div class="item"><div class="row"><span class="nm">Marinara</span><span class="dots"></span><span class="pr">18</span></div><div class="ds">Seafood mix in a Red Pasta Sauce</div></div>
      </div>
    </div>
  </section>

  <section class="page page-two">
    <div class="photo photo-pizza-two" role="img" aria-label="Photo of pizza slices"></div>
    <div class="photo photo-plate" role="img" aria-label="Photo of a white plate with fork and knife"></div>

    <div class="col" style="left:5px;top:5px;width:288px;height:605px">
      <div class="head" style="display:block">Main<small>[Served with Chips &amp; Garden Salad]</small></div>
      <div class="list" style="height:260px;margin-top:8px">
        <div class="item"><div class="row"><span class="nm">Chicken Schnitzel with Gravy</span><span class="dots"></span><span class="pr">16</span></div></div>
        <div class="item"><div class="row"><span class="nm">Veal Schnitzel with Gravy</span><span class="dots"></span><span class="pr">16</span></div></div>
        <div class="item"><div class="row"><span class="nm">Chicken Parmigiana</span><span class="dots"></span><span class="pr">17</span></div></div>
        <div class="item"><div class="row"><span class="nm">Three Cheese Parmigiana</span><span class="dots"></span><span class="pr">17</span></div><div class="ds">Topped with Parmesan, Mozzarella, Bocconcini &amp; Herbs</div></div>
        <div class="item"><div class="row"><span class="nm">Hawiian Parmigiana</span><span class="dots"></span><span class="pr">17</span></div><div class="ds">Topped with Cheese, Ham, Pineapple &amp; Herbs</div></div>
        <div class="item"><div class="row"><span class="nm">Mexican Parmigiana</span><span class="dots"></span><span class="pr">17</span></div><div class="ds">Topped with Cheese, Roasted Capsicum, Jalapenos &amp; Herbs</div></div>
        <div class="item"><div class="row"><span class="nm">Marinara Parmigiana</span><span class="dots"></span><span class="pr">19</span></div><div class="ds">Topped with Cheese, Seafood mix &amp; Herbs</div></div>
        <div class="item"><div class="row"><span class="nm">Creamy Garlic Prawn</span><span class="dots"></span><span class="pr">19</span></div><div class="ds">Tiger Prawn, Garlic, White Wine, Spices &amp; Herbs Pan fried with Creamy sauce</div></div>
      </div>
      <div class="head" style="margin-top:22px">Ribs &amp; Wings</div>
      <div class="list fill" style="margin-top:14px">
        <div class="item"><div class="row"><span class="nm">Pork Ribs</span><span class="dots"></span><span class="pr">17</span></div></div>
        <div class="item"><div class="row"><span class="nm">Beef Ribs</span><span class="dots"></span><span class="pr">15</span></div></div>
        <div class="item"><div class="row"><span class="nm">Buffalo Wings (6 Pcs)</span><span class="dots"></span><span class="pr">8</span></div></div>
        <div class="item"><div class="row"><span class="nm">BBQ Wings (6 Pcs)</span><span class="dots"></span><span class="pr">8</span></div></div>
        <div class="item"><div class="row"><span class="nm">Honey Soy wings (6 Pcs)</span><span class="dots"></span><span class="pr">8</span></div></div>
        <div class="item"><div class="row"><span class="nm">Fried Wings (6 Pcs)</span><span class="dots"></span><span class="pr">8</span></div><div class="ds">with Tomato Sauce</div></div>
        <div class="item"><div class="row"><span class="nm">Chicken Lollipop (5 Pcs)</span><span class="dots"></span><span class="pr">8</span></div><div class="ds">with Lemon Wedges</div></div>
      </div>
    </div>

    <div class="col" style="left:300px;top:8px;width:298px;height:600px">
      <div class="head" style="padding:8px 6px">The AB</div>
      <div class="list" style="height:240px;margin-top:10px">
        <div class="item"><div class="row"><span class="nm">AB Chicken</span><span class="dots"></span><span class="pr">13.95</span></div><div class="ds">Marinated Chicken, Cheese on Top of Fries, Drizzled with Ranch, BBQ &amp; Garlic Sauce</div></div>
        <div class="item"><div class="row"><span class="nm">AB Meat L</span><span class="dots"></span><span class="pr">13.95</span></div><div class="ds">Cheese, Pulled Beef, Bacon, Ham on Top of Fries, Drizzled with Ranch, BBQ &amp; Garlic Sauce</div></div>
        <div class="item"><div class="row"><span class="nm">AB Combin</span><span class="dots"></span><span class="pr">13.95</span></div><div class="ds">Cheese, Chicken, Pulled Beef, Ham on Top of Fries, Drizzled with Ranch, BBQ &amp; Garlic Sauce</div></div>
        <div class="item"><div class="row"><span class="nm">AB Veg</span><span class="dots"></span><span class="pr">13.95</span></div><div class="ds">Cheese, Tomato, Capsicum, Mushroom, Crumbed Fetta, Pineapple on Top of Fries, Drizzled with Ranch, Tomato &amp; Garlic Sauce</div></div>
        <div class="item"><div class="row"><span class="nm">AB Double</span><span class="dots"></span><span class="pr">11.95</span></div><div class="ds">Double Cheese on Top of Fries, Drizzled with Ranch, Tomato &amp; Garlic Sauce</div></div>
      </div>
      <div class="head" style="margin-top:10px;padding:6px">Dessert</div>
      <div class="list fill" style="margin-top:10px">
        <div class="item"><div class="row"><span class="nm">Chocolate Sundae</span><span class="dots"></span><span class="pr">4.95</span></div></div>
        <div class="item"><div class="row"><span class="nm">Chocohaze Calzone</span><span class="dots"></span><span class="pr">6</span></div><div class="ds">Calzone filled with Chocohaze &amp; topped with Icing Sugar</div></div>
        <div class="item"><div class="row"><span class="nm">Berry Zone</span><span class="dots"></span><span class="pr">9</span></div><div class="ds">Chocohaze Calzone filled with Mixed Berry &amp; topped with Icing Sugar</div></div>
        <div class="item"><div class="row"><span class="nm">White Volcone</span><span class="dots"></span><span class="pr">9</span></div><div class="ds">Calzone filled with White Chocolate &amp; topped with Icing Sugar</div></div>
        <div class="item"><div class="row"><span class="nm">Cookie Crumb Calzone</span><span class="dots"></span><span class="pr">9</span></div><div class="ds">Calzone rolled with Cookie Crumb, filled with White Chocolate &amp; topped with Icing Sugar</div></div>
        <div class="item"><div class="row"><span class="nm">Tropical Calzone</span><span class="dots"></span><span class="pr">9</span></div><div class="ds">Chocohaze Calzone filled with Mango and Pineapple &amp; topped with Icing Sugar</div></div>
      </div>
    </div>

    <div class="col" style="left:604px;top:6px;width:290px;height:612px">
      <div class="head" style="padding:8px 6px">Salad</div>
      <div class="list" style="height:170px;margin-top:12px">
        <div class="item"><div class="row"><span class="nm">Garden Salad</span><span class="dots"></span><span class="pr">6</span></div><div class="ds">Mixed Leaves, Tomato, Cucumber, Olives, Onion, Cucumber, Pineapple &amp; Italian dressing</div></div>
        <div class="item"><div class="row"><span class="nm">Greek Salad</span><span class="dots"></span><span class="pr">6</span></div><div class="ds">Mixed Leaves, Tomato, Cucumber, Olives, Onion, Fetta &amp; Dressed with Lemon Juice, Olive Oil, White wine vinegar</div></div>
        <div class="item"><div class="row"><span class="nm">Coleslaw</span><span class="dots"></span><span class="pr">6</span></div><div class="ds">Red Cabbages, Green Cabbage, Carrot, Onion mixed with Mayonnaise and Lemon</div></div>
        <div class="item"><div class="row"><span class="nm">Chicken Ceaser Salad</span><span class="dots"></span><span class="pr">9</span></div><div class="ds">Mixed Leaves, Chicken, Crispy Bacon, Croutons, Parmesan Cheese &amp; Ceaser Dressing</div></div>
      </div>
      <div class="head" style="margin-top:24px;padding:8px 6px">Drinks</div>
      <div class="list fill" style="margin-top:10px">
        <div class="item"><div class="row"><span class="nm">Can</span><span class="dots"></span><span class="pr">2.95</span></div><div class="ds">Cola, Diet Cola, Cola Zero, Orange Soda, Lemonade</div></div>
        <div class="item"><div class="row"><span class="nm">1.25 lit</span><span class="dots"></span><span class="pr">4.95</span></div><div class="ds">Cola, Diet Cola, Cola Zero, Orange Soda, Lemonade</div></div>
        <div class="item"><div class="row"><span class="nm">Peakside Ice Tea</span><span class="dots"></span><span class="pr">3.95</span></div></div>
        <div class="item"><div class="row"><span class="nm">Orange Juice</span><span class="dots"></span><span class="pr">4.50</span></div></div>
        <div class="item"><div class="row"><span class="nm">Ginger Beer</span><span class="dots"></span><span class="pr">3.95</span></div></div>
        <div class="item"><div class="row"><span class="nm">Clearspring Water</span><span class="dots"></span><span class="pr">2.50</span></div></div>
        <div class="item"><div class="row"><span class="nm">Voltra Energy Drink (375 ml)</span><span class="dots"></span><span class="pr">3.95</span></div></div>
      </div>
      <div class="contact" style="margin-top:10px">
        <h3>Contact Details</h3>
        <div>Rinzo Pizza &amp; Pasta, 114 Harbour<br>View Rd, Westmere</div>
        <div class="phone">07 3540 2281</div>
        <div class="phone">www.rinzo.com.au</div>
      </div>
    </div>

    <div class="col" style="left:903px;top:8px;width:293px;height:450px">
      <div class="head" style="padding:8px 6px">Dinner Pack <span class="price" style="font-size:30px">$25</span></div>
      <div class="list" style="height:122px;margin-top:8px">
        <div class="item"><div class="nm">Pizza Pack</div><div class="ds">Cheesy Garlic Bread, Any Large Pizza (Excl Premium range), Any Dessert or 1.25 lit</div></div>
        <div class="item"><div class="nm">Pasta Pack</div><div class="ds">Curly Fries, Any Pasta, Any Dessert or 1.25 lit</div></div>
        <div class="item"><div class="nm">Parmi Pack</div><div class="ds">Chips, Any Parmigiana, Any Dessert or 1.25 lit</div></div>
        <div class="item"><div class="nm">Ribs &amp; Wings Pack</div><div class="ds">Chips, Any Wings, Ribs (Pork or Beef)</div></div>
      </div>
      <div class="head" style="margin-top:10px;padding:4px 6px;font-size:32px">Deals <span class="price" style="font-size:20px;line-height:1;text-align:center">FREE DELIVERY<br><span style="font-size:16px">$40 and Over</span></span></div>
      <div class="list fill" style="margin-top:10px">
        <div class="item"><div class="row"><span class="nm">Party Deal</span><span style="flex:1"></span><span class="pr">$54.95</span></div><div class="ds">3 Large Pizza or Pasta, 2 Garlic Bread &amp; 1.25 lit Drink</div></div>
        <div class="item"><div class="row"><span class="nm">Family Deal</span><span style="flex:1"></span><span class="pr">$39.95</span></div><div class="ds">2 Large Pizza or Pasta, 2 Garlic Bread, 1.25 lit drink</div></div>
        <div class="item"><div class="row"><span class="nm">Couple Deal</span><span style="flex:1"></span><span class="pr">$24.95</span></div><div class="ds">1 Family Pizza, 1 Garlic Bread, 1.25 lit Drink</div></div>
        <div class="item"><div class="row"><span class="nm">Single Deal</span><span style="flex:1"></span><span class="pr">$19.95</span></div><div class="ds">1 Large Pizza or Pasta, 1 Garlic Bread, 1 can drink</div></div>
        <div class="item"><div class="row"><span class="nm">Small Deal</span><span style="flex:1"></span><span class="pr">$14.95</span></div><div class="ds">1 Small Pizza, 1 Garlic Bread, 1 can drink - $14.95</div></div>
      </div>
      <div class="terms" style="margin-top:10px">Terms &amp; Condition:<br>&nbsp;&nbsp;&nbsp;&nbsp;(Large Pizza Excludes Premium &amp; Seafood range)</div>
    </div>

    <div class="brand"><i></i>Rinzo</div>
  </section>
</div>
</body>
</html>
```